Wedding Thank You post card

We would like to design a thank you post card for our wedding guests.
We want it to be a classic style with our photo and a simple 'Thank you' written and then Tom and Sylvia 15.03.2014' Where the writing does not obstruct our image.
We need 140 post cards
Sorry for the delay please find some photos you can use for the design process. One or all photos can be used. Thank you
Wedding

```html
<!DOCTYPE html>
<html lang="en">
<head>
<meta charset="utf-8">
<title>Thank You Card – Tom and Sylvia</title>
<link href="https://fonts.googleapis.com/css2?family=Pinyon+Script&family=Great+Vibes&display=swap" rel="stylesheet">
<style>
  :root {
    --paper: #ffffff;
    --silver-light: #eeeeee;
    --silver: #c9c9c9;
    --silver-dark: #a9a9a9;
    --cocoa: #3b2a22;
    --cocoa-deep: #2e201a;
    --cream: #f3ead8;
    --ink: #3a2a22;
    --photo-warm: #c98a3a;
    --photo-deep: #4a2c17;
  }
  html, body {
    margin: 0;
    padding: 0;
    overflow: hidden;
    background: var(--paper);
  }
  .card {
    position: relative;
    width: 1200px;
    height: 929px;
    overflow: hidden;
    background: var(--paper);
  }
  .top-flourish {
    position: absolute;
    left: 0; top: 0;
    width: 1200px; height: 284px;
    background: linear-gradient(180deg, var(--silver-light) 0%, #f6f6f6 60%, var(--paper) 100%);
  }
  .header-rule {
    position: absolute;
    left: 0; top: 286px;
    width: 1200px; height: 20px;
    background: linear-gradient(180deg, var(--silver) 0%, #e2e2e2 100%);
  }
  .name-plaque {
    position: absolute;
    left: 102px; top: 176px;
    width: 280px; height: 186px;
  }
  .name-plaque svg { position: absolute; inset: 0; }
  .name-plaque .names {
    position: absolute;
    inset: 0;
    display: flex;
    flex-direction: column;
    align-items: center;
    justify-content: center;
    font-family: "Great Vibes", cursive;
    color: var(--cream);
    font-size: 50px;
    line-height: 48px;
  }
  .name-plaque .names .joiner { font-size: 38px; line-height: 38px; }
  .wedding-date {
    position: absolute;
    left: 405px; top: 262px;
    font-family: "Great Vibes", cursive;
    font-size: 32px;
    color: var(--ink);
    letter-spacing: 1px;
  }
  .photo-frame {
    position: absolute;
    left: 655px; top: 110px;
    width: 420px; height: 530px;
    background: var(--paper);
    box-shadow: 0 4px 14px rgba(0,0,0,0.28);
    transform: rotate(-7deg);
  }
  .photo-frame .photo {
    position: absolute;
    left: 20px; top: 20px; right: 20px; bottom: 20px;
    background: radial-gradient(ellipse at 30% 30%, #e8b463 0%, var(--photo-warm) 40%, var(--photo-deep) 100%);
  }
  .thank-you {
    position: absolute;
    left: 92px; top: 425px;
    font-family: "Pinyon Script", cursive;
    font-size: 124px;
    line-height: 1;
    color: var(--ink);
    margin: 0;
    font-weight: 400;
  }
  .divider {
    position: absolute;
    left: 0; width: 1200px;
    background: var(--silver);
  }
  .divider.upper { top: 632px; height: 3px; }
  .divider.lower { top: 668px; height: 8px; background: var(--silver-dark); }
  .bottom-flourish {
    position: absolute;
    left: 0; top: 684px;
    width: 1200px; height: 245px;
    background: linear-gradient(180deg, var(--cocoa) 0%, var(--cocoa-deep) 100%);
  }
</style>
</head>
<body>
  <div class="card">
    <div class="top-flourish" role="img" aria-label="Soft silver damask flourish pattern"></div>
    <div class="header-rule"></div>

    <div class="divider upper"></div>
    <div class="divider lower"></div>
    <div class="bottom-flourish" role="img" aria-label="Dark brown damask flourish pattern"></div>

    <div class="name-plaque">
      <svg width="280" height="186" viewBox="0 0 280 186">
        <path d="M24 4 H256 Q256 24 276 24 V162 Q256 162 256 182 H24 Q24 162 4 162 V24 Q24 24 24 4 Z"
              fill="var(--cocoa)" stroke="var(--silver)" stroke-width="3"/>
      </svg>
      <div class="names">
        <span>Tom</span>
        <span class="joiner">and</span>
        <span>Sylvia</span>
      </div>
    </div>

    <div class="wedding-date">15.03.2014</div>

    <div class="photo-frame">
      <div class="photo" role="img" aria-label="Wedding couple photograph in warm golden light"></div>
    </div>

    <h1 class="thank-you">Thank You</h1>
  </div>
</body>
</html>
```